Redesign a car and car-insurance Home Page

Existing Home Page can be found here: www.wheelnook.example.

Wheelnook.example is both a car forum as well as a lead generation system for people looking to buy new cars or get insurance for existing cars. Users can simply sign up and be contacted by dealers/insurers. The lead generation aspect is very prominent, however, we want to change this to make the forum/more social and community aspect of the site more prominent. To that end, we'd like a design that reflects both. We like the minimalist type designs that draw your attention to the important parts and don't have unnecessary boxes or text. We want a modern and interactive look and feel. We are open to your creativity therefore we will not set any limitations.

*creating or updating our logo is welcomed.

We like http://drivelume.example/, but as I've said, we need to make the forum more prominent as well as links to the forms for users who are looking for vehicles. We also want to make clear exactly what we do on the front page.
Showing youtube videos is also desirable (maybe in a latest video section).
Updates

I am not a fan of stock photos. Maybe just one the most. 

Project Deadline Extended

Target Market(s)

People who are looking to buy new cars or save on car insurance. Want it to be applicable across all lines

Industry/Entity Type

Insurance

Requirements
Nice to have
• I would love to have the forum and car review section to look like that of www.motorpiq.example
Should not have
• Too much if any stock photos. Maybe one and this depends on how it is placed and portrayed.

```html
<!DOCTYPE html>
<html lang="en">
<head>
<meta charset="utf-8">
<title>Wheelnook — Buy. Insure. Drive.</title>
<link href="https://fonts.googleapis.com/css2?family=Inter:wght@400;700;800&family=Questrial&family=Varela+Round&display=swap" rel="stylesheet">
<style>
:root{
  --teal:#4fc6cf;
  --teal-dark:#2fb0bb;
  --green:#8fd13a;
  --green-edge:#6fae22;
  --orange:#f6b23e;
  --orange-text:#f07a23;
  --ink:#222;
  --muted:#555;
  --link:#2a9bb0;
  --cream:#fdf8e8;
  --pale:#fffdf5;
  --rule:#e3dccb;
  --band:#e4e4e4;
  --footer:#2f2f2f;
}
*{box-sizing:border-box;margin:0;padding:0}
html,body{width:1200px;height:3386px;overflow:hidden}
body{font-family:"Questrial",sans-serif;color:var(--ink);background:#fff;position:relative}
a{color:inherit;text-decoration:none}

/* header */
.site-header{height:105px;background:var(--teal);display:flex;align-items:center;padding:0 120px;color:#fff;white-space:nowrap}
.brand{font-family:"Questrial",sans-serif;font-size:46px;color:#fff;margin-right:56px;flex:none}
.main-nav{display:flex;gap:34px;font-size:18px;flex:none}
.account-nav{margin-left:auto;display:flex;gap:28px;font-size:18px;flex:none}
.main-nav a,.account-nav a{flex:none}

/* hero */
.hero{height:570px;text-align:center;padding-top:112px}
.hero h1{font-family:"Inter",sans-serif;font-weight:800;font-size:104px;letter-spacing:-3px;line-height:1}
.hero p{width:600px;margin:68px auto 0;font-size:24px;line-height:1.32;color:#333}
.hero-actions{margin-top:40px;display:flex;justify-content:center;gap:28px}
.btn{display:inline-flex;align-items:center;justify-content:center;height:58px;padding:0 46px;background:var(--green);border:2px solid var(--green-edge);border-radius:6px;font-size:21px;color:#1f3a05;white-space:nowrap}

/* community */
.community{height:863px;background:var(--cream);display:flex;gap:72px;padding:78px 112px 0 120px}
.column{flex:1}
.column-head{display:flex;justify-content:space-between;align-items:baseline;padding-bottom:26px}
.column-head h2{font-family:"Inter",sans-serif;font-weight:700;font-size:26px}
.column-head a{color:var(--link);font-size:18px}
.post{display:flex;gap:22px;padding:28px 0 22px;border-bottom:1px solid var(--rule);height:218px}
.post:last-child{border-bottom:none}
.thumb{flex:none;border-radius:3px;background:linear-gradient(180deg,#8a9299 0%,#4b535a 55%,#2a2f33 100%)}
.review .thumb{width:180px;height:150px}
.question .thumb{width:94px;height:72px}
.post-body{flex:1;display:flex;flex-direction:column}
.post-title{color:var(--link);font-size:20px;line-height:1.2}
.stars{color:#f4b400;font-size:20px;letter-spacing:2px;margin:4px 0 6px}
.excerpt{font-size:15px;line-height:1.45;color:#333;margin-top:8px}
.more{align-self:flex-end;margin-top:auto;color:var(--link);font-size:15px}

/* steps */
.steps{position:relative;height:712px;background:var(--pale)}
.steps.insurance{height:740px;background:#fff;border-top:1px solid #ddd}
.steps svg{position:absolute;left:0;top:0}
.bubble{position:absolute;text-align:center;color:#fff;font-size:15px;line-height:1.35}
.bubble h3{font-weight:400;font-size:20px;line-height:1.25;margin-bottom:10px}
.insurance .bubble{color:#2b1a05}
.steps-title{position:absolute;font-family:"Varela Round",sans-serif;text-align:center;line-height:1.05}
.car .steps-title{color:var(--teal-dark);font-size:46px}
.insurance .steps-title{color:var(--orange-text);font-size:48px}
.steps .btn{position:absolute;left:520px;width:160px;padding:0}

/* partners */
.partners{position:absolute;top:2990px;left:0;width:1200px;height:150px;background:var(--band);display:flex;justify-content:center;align-items:center;gap:90px}
.partner-badge{width:120px;height:30px;border-radius:4px;background:#bdbdbd}

/* footer */
.site-footer{position:absolute;top:3140px;left:0;width:1200px;height:246px;background:var(--footer);color:#ddd;text-align:center;padding-top:38px}
.site-footer .brand{display:block;margin:0;font-size:50px;color:#bbb}
.social{display:flex;justify-content:center;gap:12px;margin:12px 0 14px}
.social span{width:24px;height:24px;border-radius:50%;background:#777}
.footer-nav{font-size:17px}
.footer-nav a{padding:0 8px}
.copyright{font-size:14px;color:#aaa;margin-top:8px}
</style>
</head>
<body>

<header class="site-header">
  <a class="brand" href="#">Wheelnook</a>
  <nav class="main-nav">
    <a href="#">Get Insurance</a><a href="#">New &amp; Used Cars</a><a href="#">Blog</a><a href="#">Questions</a>
  </nav>
  <nav class="account-nav"><a href="#">Login</a><a href="#">Sign up</a></nav>
</header>

<section class="hero">
  <h1>Buy. Insure. Drive.</h1>
  <p>At wheelnook we make it easy to find your next car (new or used) along with better car insurance, while giving you the best possible deal.</p>
  <div class="hero-actions">
    <a class="btn" href="#">New &amp; Used Cars</a>
    <a class="btn" href="#">Get Insurance</a>
  </div>
</section>

<section class="community">
  <div class="column">
    <div class="column-head"><h2>Car Reviews</h2><a href="#">Review your car</a></div>
    <article class="post review">
      <div class="thumb" role="img" aria-label="Photo of a dark sedan, front view"></div>
      <div class="post-body">
        <a class="post-title" href="#">2012 Varela R37 Review</a>
        <div class="stars">★★★★★</div>
        <p class="excerpt">I just recently bought this car, at first I did not want to get a Varela but then I drove it around was pretty...</p>
        <a class="more" href="#">Read full review...</a>
      </div>
    </article>
    <article class="post review">
      <div class="thumb" role="img" aria-label="Photo of a dark sedan, front view"></div>
      <div class="post-body">
        <a class="post-title" href="#">2012 Varela R37 Review</a>
        <div class="stars">★★★★★</div>
        <p class="excerpt">I just recently bought this car, at first I did not want to get a Varela but then I drove it around was pretty...</p>
        <a class="more" href="#">Read full review...</a>
      </div>
    </article>
    <article class="post review">
      <div class="thumb" role="img" aria-label="Photo of a dark sedan, front view"></div>
      <div class="post-body">
        <a class="post-title" href="#">2012 Varela R37 Review</a>
        <div class="stars">★★★★★</div>
        <p class="excerpt">I just recently bought this car, at first I did not want to get a Varela but then I drove it around was pretty...</p>
        <a class="more" href="#">Read full review...</a>
      </div>
    </article>
  </div>

  <div class="column">
    <div class="column-head"><h2>Latest Questions</h2><a href="#">Ask a question</a></div>
    <article class="post question">
      <div class="thumb" role="img" aria-label="Small photo of a dark sedan"></div>
      <div class="post-body">
        <a class="post-title" href="#">What is gas tank size on a 1981 Kessan Arrow GT?</a>
        <p class="excerpt">I just recently bought this car, at first I did not want to get one but then I drove it around and was pretty impressed. I still like the car how...</p>
        <a class="more" href="#">Read more...</a>
      </div>
    </article>
    <article class="post question">
      <div class="thumb" role="img" aria-label="Small photo of a dark sedan"></div>
      <div class="post-body">
        <a class="post-title" href="#">What is gas tank size on a 1981 Kessan Arrow GT?</a>
        <p class="excerpt">I just recently bought this car, at first I did not want to get one but then I drove it around and was pretty impressed. I still like the car how...</p>
        <a class="more" href="#">Read more...</a>
      </div>
    </article>
    <article class="post question">
      <div class="thumb" role="img" aria-label="Small photo of a dark sedan"></div>
      <div class="post-body">
        <a class="post-title" href="#">What vehicle would YOU choose to survive a Zombie Apocalypse?</a>
        <p class="excerpt">I just recently bought this car, at first I did not want to get one but then I drove it around and was pretty impressed. I still like the car how...</p>
        <a class="more" href="#">Read more...</a>
      </div>
    </article>
  </div>
</section>

<section class="steps car">
  <svg width="1200" height="712" viewBox="0 0 1200 712" aria-hidden="true">
    <g fill="var(--teal)">
      <ellipse cx="600" cy="194" rx="160" ry="112"/>
      <path d="M570 295 L592 372 L625 298 Z"/>
      <ellipse cx="262" cy="330" rx="150" ry="103"/>
      <path d="M372 385 L440 412 L395 355 Z"/>
      <ellipse cx="893" cy="362" rx="150" ry="100"/>
      <path d="M775 395 L770 448 L810 428 Z"/>
    </g>
  </svg>
  <div class="bubble" style="left:470px;top:115px;width:260px">
    <h3>We contact Wheelnook's dealer network</h3>
    We send out your selection to our network of dealers.
  </div>
  <div class="bubble" style="left:142px;top:268px;width:240px">
    <h3>Select vehicle and give us your information</h3>
    Just tell us the make and model and how to get in touch with you.
  </div>
  <div class="bubble" style="left:773px;top:295px;width:240px">
    <h3>Dealers contact you with offers</h3>
    The dealers contact you with their best offers so you can choose the best deal.
  </div>
  <div class="steps-title" style="left:455px;top:418px;width:290px">Looking for a new car.</div>
  <a class="btn" href="#" style="top:543px">Register Here</a>
</section>

<section class="steps insurance">
  <svg width="1200" height="740" viewBox="0 0 1200 740" aria-hidden="true">
    <g fill="var(--orange)">
      <ellipse cx="262" cy="330" rx="150" ry="103"/>
      <path d="M370 270 L440 232 L390 300 Z"/>
      <ellipse cx="893" cy="330" rx="150" ry="103"/>
      <path d="M830 235 L790 195 L860 232 Z"/>
      <ellipse cx="600" cy="525" rx="160" ry="112"/>
      <path d="M560 420 L600 362 L630 418 Z"/>
    </g>
  </svg>
  <a class="btn" href="#" style="top:96px">Register Here</a>
  <div class="steps-title" style="left:450px;top:180px;width:300px">Looking for<br>new<br>insurance</div>
  <div class="bubble" style="left:142px;top:265px;width:240px">
    <h3>Give us your vehicle information</h3>
    For the best insurance quotes at comparable rates, all we need is your vehicle information along with your contact information.
  </div>
  <div class="bubble" style="left:773px;top:270px;width:240px">
    <h3>You receive insurance quotes</h3>
    They contact you with the best coverage at the best prices to suit your needs. You compare, you decide.
  </div>
  <div class="bubble" style="left:480px;top:470px;width:240px">
    <h3>We contact insurance agents</h3>
    We notify our experienced network of insurance agents.
  </div>
</section>

<section class="partners" aria-label="Partners">
  <span class="partner-badge"></span><span class="partner-badge"></span><span class="partner-badge"></span><span class="partner-badge"></span>
</section>

<footer class="site-footer">
  <span class="brand">Wheelnook</span>
  <div class="social"><span></span><span></span><span></span></div>
  <nav class="footer-nav"><a href="#">About</a>|<a href="#">Contact Us</a>|<a href="#">Privacy Policy</a>|<a href="#">Blog</a></nav>
  <p class="copyright">© 2013 Wheelnook Inc. All Rights Reserved.</p>
</footer>

</body>
</html>
```